Veltarum

Standard Business Card design.
Sample two-sided design uploaded. White front, Black back.
Would like white shield to be on all black background side.
Willing to look at a couple creative designs, but nothing crazy.
Preference for a classic, confident, strong design.

```html
<!DOCTYPE html>
<html lang="en">
<head>
<meta charset="UTF-8">
<title>Veltarum Business Card</title>
<link href="https://fonts.googleapis.com/css2?family=Montserrat:wght@400;500;700&display=swap" rel="stylesheet">
<style>
  :root {
    --ink: #111111;
    --paper: #f7f7f5;
    --backdrop: #d9d9d7;
    --rule: #333333;
    --muted: #2b2b2b;
    --ghost: #e6e6e4;
  }
  * { margin: 0; padding: 0; box-sizing: border-box; }
  html, body {
    width: 1200px; height: 801px; overflow: hidden;
    background: var(--backdrop);
    font-family: "Montserrat", sans-serif;
  }
  .stage {
    position: relative; width: 1200px; height: 801px;
    display: flex; justify-content: center; align-items: center; gap: 80px;
  }
  .card {
    position: relative; width: 300px; height: 525px;
    box-shadow: 0 6px 18px rgba(0,0,0,0.18);
  }
  .card--back { background: var(--ink); color: #fff; }
  .card--front { background: var(--paper); color: var(--ink); }

  .back-mark {
    position: absolute; left: 0; right: 0; top: 50%;
    transform: translateY(-50%);
    display: flex; flex-direction: column; align-items: center;
  }
  .back-mark .wordmark {
    font-weight: 700; font-size: 32px; letter-spacing: 3px; color: #fff;
  }
  .back-mark .mark-rule {
    width: 190px; height: 1px; background: #fff; margin-top: 10px;
  }

  .front-rule {
    position: absolute; left: 36px; top: 0; bottom: 0;
    width: 1px; background: var(--rule);
  }
  .front-mark {
    position: absolute; left: 56px; top: 34px;
  }
  .front-mark .wordmark {
    font-weight: 700; font-size: 20px; letter-spacing: 2px; color: var(--ink);
  }
  .front-mark .mark-rule {
    width: 140px; height: 1px; background: var(--ink); margin-top: 7px;
  }
  .ghost-disc {
    position: absolute; left: 86px; top: 110px;
    width: 150px; height: 150px; border-radius: 50%;
    background: var(--ghost);
  }
  .identity { position: absolute; left: 56px; top: 312px; }
  .identity .name { font-weight: 700; font-size: 17px; letter-spacing: 0.5px; }
  .identity .role { font-weight: 400; font-size: 13px; color: var(--muted); margin-top: 2px; }
  .contacts {
    position: absolute; left: 56px; top: 380px; list-style: none;
    font-size: 12.5px; line-height: 20px; color: var(--muted);
  }
  .contacts li { display: flex; align-items: center; gap: 8px; }
  .contacts .icon { width: 11px; height: 11px; flex: none; }
  .contacts .spacer { width: 11px; flex: none; }
</style>
</head>
<body>
<main class="stage">
  <section class="card card--back" aria-label="Card back">
    <div class="back-mark">
      <span class="wordmark">VELTARUM</span>
      <span class="mark-rule"></span>
    </div>
  </section>

  <section class="card card--front" aria-label="Card front">
    <span class="front-rule"></span>
    <div class="front-mark">
      <span class="wordmark">VELTARUM</span>
      <div class="mark-rule"></div>
    </div>
    <span class="ghost-disc"></span>
    <div class="identity">
      <p class="name">YOUR NAME</p>
      <p class="role">Designation</p>
    </div>
    <ul class="contacts">
      <li>
        <svg class="icon" viewBox="0 0 12 12"><path d="M2 1l2 0 1 3-1.3 1a6 6 0 0 0 3.3 3.3L8 7l3 1v2c0 .6-.4 1-1 1A9 9 0 0 1 1 2c0-.6.4-1 1-1z" fill="#222"/></svg>
        +1 123 456 789
      </li>
      <li>
        <svg class="icon" viewBox="0 0 12 12"><rect x="0.5" y="2" width="11" height="8" fill="#222"/><path d="M0.5 2l5.5 4.5L11.5 2" stroke="#f7f7f5" stroke-width="1" fill="none"/></svg>
        yourname@email.com
      </li>
      <li>
        <svg class="icon" viewBox="0 0 12 12"><circle cx="6" cy="6" r="5" fill="#222"/><path d="M1 6h10M6 1c-2.5 3-2.5 7 0 10M6 1c2.5 3 2.5 7 0 10" stroke="#f7f7f5" stroke-width="0.8" fill="none"/></svg>
        www.veltarumgroup.com
      </li>
      <li><span class="spacer"></span>Address Line One,</li>
      <li><span class="spacer"></span>City, State, Country</li>
    </ul>
  </section>
</main>
</body>
</html>
```